Design for Screen Wash Tablet Tube New product

I have a tube which holds screenwash tablets which I need Label created for... Label is 90mm x 90mm. It must include
> logo attached,
>the catchphrase ( drop,dissolve,wash. )
>6 Tablets inside
>1 Tablet makes 5 litres screen wash
>Room for ingredients section( around 20 words)
> Caution - Harmful if swallowed. May cause skin Irritation or eye damage. Do not eat,drink or smoke when using this product. If medical advice is needed have product packaging to hand. Store in a clean dry place.
>Keep out of reach of Children
>Barcode area
>Directions of use
Place tablet in Screenwash bottle
Simply add water
>Product will take approximately 5-10 minutes to fully dissolve.
>3 harmful logo attached
>Cherry Fragrance
retail sector - grocery fmcg and car/auto stores
car care

```html
<!DOCTYPE html>
<html lang="en">
<head>
<meta charset="utf-8">
<title>ClearVale Screenwash Tablets – Tube Label</title>
<link rel="stylesheet" href="https://fonts.googleapis.com/css2?family=Anton&family=Oswald:wght@600&family=Poppins:wght@300;400;600&display=swap">
<style>
  :root {
    --backdrop: #8c8c8c;
    --teal: #17786f;
    --teal-deep: #0d4f4a;
    --teal-light: #2a9a8e;
    --red: #d7192a;
    --red-dark: #a50f1c;
    --white: #ffffff;
    --yellow: #f2d21a;
    --cherry: #c2186b;
    --ink: #1b2a2a;
  }
  * { box-sizing: border-box; margin: 0; padding: 0; }
  html, body { width: 1200px; height: 900px; overflow: hidden; }
  body {
    background: var(--backdrop);
    font-family: "Poppins", sans-serif;
    display: flex; align-items: center; justify-content: center;
  }
  .label {
    width: 780px; height: 780px;
    display: flex;
    box-shadow: 0 10px 30px rgba(0,0,0,.25);
  }
  .panel { position: relative; width: 390px; height: 780px; overflow: hidden; }

  /* ---------- Info panel ---------- */
  .info-panel {
    background: linear-gradient(180deg, var(--teal-light) 0%, var(--teal) 45%, var(--teal-deep) 100%);
    color: var(--white);
    padding: 44px 28px 0 34px;
    font-weight: 300;
    font-size: 15.5px;
    line-height: 1.45;
  }
  .info-block { margin-bottom: 28px; }
  .info-panel .hazards {
    display: flex; gap: 18px; margin-top: 6px;
  }
  .hazard { width: 62px; height: 62px; }
  .info-base {
    position: absolute; left: 0; bottom: 0; width: 390px; height: 190px;
  }

  /* ---------- Front panel ---------- */
  .front-panel { background: var(--white); text-align: center; }
  .brand {
    margin: 30px auto 0;
    width: 200px; height: 62px;
    border: 2px solid var(--teal);
    border-radius: 50%;
    display: flex; align-items: center; justify-content: center; gap: 8px;
  }
  .brand-dot { width: 10px; height: 10px; border-radius: 50%; background: var(--red); }
  .brand-name {
    font-family: "Poppins", sans-serif; font-weight: 600;
    font-size: 22px; color: var(--red);
  }
  .product-title {
    font-family: "Anton", sans-serif;
    color: var(--red);
    -webkit-text-stroke: 2px var(--red-dark);
    text-shadow: 0 0 0 var(--white), 2px 2px 0 var(--white), -2px -2px 0 var(--white), 2px -2px 0 var(--white), -2px 2px 0 var(--white), 3px 4px 4px rgba(0,0,0,.35);
    line-height: .95;
    margin-top: 22px;
  }
  .product-title .line-1 { display: block; font-size: 44px; letter-spacing: .5px; }
  .product-title .line-2 { display: block; font-size: 76px; letter-spacing: 1px; }
  .fragrance {
    margin-top: 8px;
    font-size: 17px; color: var(--cherry); font-weight: 400; letter-spacing: .5px;
  }
  .car-photo {
    position: absolute; left: 0; top: 330px; width: 390px; height: 230px;
    background: radial-gradient(ellipse at 35% 60%, #3a8f97 0%, #174a52 40%, #0a1a1e 85%);
  }
  .front-base { position: absolute; left: 0; top: 470px; width: 390px; height: 310px; }
  .front-copy {
    position: absolute; left: 0; top: 590px; width: 390px; color: var(--white);
  }
  .catchphrase {
    font-family: "Oswald", sans-serif; font-weight: 600;
    font-size: 36px; color: var(--yellow); letter-spacing: .3px;
    text-shadow: 1px 2px 2px rgba(0,0,0,.4);
  }
  .count {
    font-family: "Oswald", sans-serif; font-weight: 600;
    font-size: 24px; margin-top: 2px;
  }
  .yield { font-size: 17px; line-height: 1.2; margin-top: 6px; }
</style>
</head>
<body>
  <main class="label">
    <section class="panel info-panel">
      <p class="info-block ingredients">Ingredients: Lorem ipsum dolor sit amet, consectetuer adipiscing elit, sed diam nonummy nibh euismod tincidunt ut laoreet dolore magna aliquam erat volutpat. Ut wisi enim.</p>
      <p class="info-block directions">Directions of use<br>Place tablet in Screenwash bottle<br>Simply add water<br>Product will take approximately 5-10 minutes to fully dissolve.</p>
      <p class="info-block caution">Caution - Harmful if swallowed. May cause skin Irritation or eye damage. Do not eat,drink or smoke when using this product. If medical advice is needed have product packaging to hand. Store in a clean dry place.</p>
      <div class="hazards">
        <svg class="hazard" viewBox="0 0 62 62" role="img" aria-label="Corrosive hazard pictogram">
          <rect x="11" y="11" width="40" height="40" transform="rotate(45 31 31)" fill="#fff" stroke="#d7192a" stroke-width="4"/>
          <rect x="20" y="26" width="22" height="12" rx="2" fill="#cfcfcf"/>
        </svg>
        <svg class="hazard" viewBox="0 0 62 62" role="img" aria-label="Environmental hazard pictogram">
          <rect x="11" y="11" width="40" height="40" transform="rotate(45 31 31)" fill="#fff" stroke="#d7192a" stroke-width="4"/>
          <rect x="20" y="24" width="22" height="16" rx="2" fill="#cfcfcf"/>
        </svg>
        <svg class="hazard" viewBox="0 0 62 62" role="img" aria-label="Exclamation mark hazard pictogram">
          <rect x="11" y="11" width="40" height="40" transform="rotate(45 31 31)" fill="#fff" stroke="#d7192a" stroke-width="4"/>
          <rect x="28.5" y="18" width="5" height="18" rx="2" fill="#111"/>
          <circle cx="31" cy="42" r="3" fill="#111"/>
        </svg>
      </div>
      <svg class="info-base" viewBox="0 0 390 190" aria-hidden="true">
        <path d="M0 90 C120 40 260 20 390 0 L390 190 L0 190 Z" fill="#d7192a"/>
        <path d="M0 100 C120 52 260 32 390 12 L390 190 L0 190 Z" fill="#ffffff"/>
      </svg>
    </section>

    <section class="panel front-panel">
      <div class="brand"><span class="brand-dot"></span><span class="brand-name">ClearVale</span></div>
      <h1 class="product-title"><span class="line-1">SCREENWASH</span><span class="line-2">TABLETS</span></h1>
      <p class="fragrance">Cherry Fragrance</p>
      <div class="car-photo" role="img" aria-label="Photo of a glossy dark sports car front with headlight"></div>
      <svg class="front-base" viewBox="0 0 390 310" aria-hidden="true">
        <path d="M0 40 C140 80 280 40 390 0 L390 310 L0 310 Z" fill="#0d4f4a"/>
        <path d="M0 80 C150 110 290 70 390 40 L390 310 L0 310 Z" fill="#17786f"/>
        <path d="M0 300 C150 280 280 255 390 230 L390 244 C280 270 150 292 0 312 Z" fill="#d7192a"/>
        <path d="M0 312 C150 292 280 270 390 244 L390 310 L0 310 Z" fill="#ffffff"/>
      </svg>
      <div class="front-copy">
        <p class="catchphrase">Drop,Dissolve,Wash</p>
        <p class="count">6 Tablets inside</p>
        <p class="yield">1 Tablet makes<br>5 litres screen wash</p>
      </div>
    </section>
  </main>
</body>
</html>
```